Town Wordpress Design Project

Hi,
I am looking for someone to completely start from scratch on a website for a town in Texas named Marblefork Vale. I designed their last website about 4 years ago but am not able to give them what I would like to with my abilities. I need a wordpress website that is web 2.0 in design while still being creative. Their current website can be seen at www.marbleforkvale.us. They like such websites by a company named MuniBolt, you can view their town website portfolio here: http://www.munibolt.com/index.aspx?NID=137. I would need all of the pages and info that is on their current site to be moved to the new site that I am hoping you can create for me. I want a much cleaner, nicer, and simpler navigation panel, while hiding links in drop down menus. I also want to include a calendar where they could post upcoming events and would want them to be able to add submit-able forms whenever they would need to. A search option would also be nice. I know that this is a design community, but if you could code the site as well or know someone who can, please let me know. Their Town Logo can be found attached, and the font in which you spell out their town name is totally up to you. They want their Agenda and Minutes to display like this: http://www.qdvwb.com/index.aspx?NID=266. Let me know if you have any further questions...
If at all possible, I wouldn't mind the design to be designed in such a way that making it "responsive" someday would be easily possible...
Reason: More time needed for some designers...
Reason: Additional time needed...

```html
<!DOCTYPE html>
<html lang="en">
<head>
<meta charset="utf-8">
<title>Town of Marblefork Vale Texas</title>
<link href="https://fonts.googleapis.com/css2?family=Oswald:wght@300;400&family=Ubuntu:wght@400&display=swap" rel="stylesheet">
<style>
:root{
  --crimson:#c0163a;
  --wine:#7a0d26;
  --deep:#5c0a1c;
  --ink:#111;
  --grey:#8a8a8a;
  --line:#d8d8d8;
  --panel:#f6f5f5;
}
*{box-sizing:border-box;margin:0;padding:0}
html,body{width:1200px;height:1013px;overflow:hidden;background:#fff}
body{position:relative;font-family:Arial,Helvetica,sans-serif;color:var(--ink)}
.abs{position:absolute}
.toplinks{top:7px;left:489px;display:flex;font-size:9.5px;font-weight:bold;color:var(--wine);white-space:nowrap}
.toplinks span{margin-right:13px}
.toplinks span:nth-child(4){margin-right:24px}
.seal{left:114px;top:21px;width:154px;height:154px;border-radius:50%;border:6px solid #111;display:flex;align-items:center;justify-content:center;text-align:center;font-family:'Oswald',sans-serif;font-weight:400;font-size:17px;color:var(--ink);line-height:1.1}
.title{left:291px;top:58px;font-family:'Oswald',sans-serif;font-weight:300;line-height:1}
.title .t1{font-size:40px;color:var(--ink);letter-spacing:-1px}
.title .t2{font-size:48px;color:var(--wine);letter-spacing:-1px;margin-top:2px}
.phone{left:845px;top:164px;display:flex;align-items:center;gap:6px;font-size:19px;font-weight:bold;color:var(--grey)}
.social{left:990px;top:168px;display:flex;gap:12px;font-family:'Ubuntu',sans-serif;font-size:10px;color:var(--grey);white-space:nowrap}
.band{left:0;top:199px;width:1200px;height:289px;background:linear-gradient(180deg,#8c0f2a 0,#a5122f 30px,var(--crimson) 31px,#b8143a 100%)}
.nav{left:100px;top:199px;height:30px;display:flex;align-items:center;font-family:'Oswald',sans-serif;font-size:15px;color:#fff;letter-spacing:-.3px}
.nav span{position:absolute;white-space:nowrap;top:4px}
.search{left:830px;top:201px;width:263px;height:24px;background:#fff;font-size:12px;color:var(--crimson);padding:5px 6px}
.search i{position:absolute;right:0;top:5px;width:28px;height:14px;border-left:1px solid var(--crimson)}
.search i:after{content:"";position:absolute;left:10px;top:2px;border-left:7px solid var(--ink);border-top:5px solid transparent;border-bottom:5px solid transparent}
.photo{left:100px;top:229px;width:1000px;height:259px;background:linear-gradient(180deg,#a9b39c 0,#c7a38a 35%,#b48b74 60%,#4f6a34 100%)}
.news{left:847px;top:295px;width:253px;height:193px;background:rgba(255,255,255,.9);border-top-left-radius:14px;border-top-right-radius:14px}
.ptitle{font-family:'Oswald',sans-serif;font-weight:300;font-size:20px;letter-spacing:-.5px;white-space:nowrap}
.item{font-family:'Ubuntu',sans-serif;font-size:11.5px;line-height:14.5px;letter-spacing:.2px}
.news .ptitle{position:absolute;left:47px;top:8px;color:var(--wine)}
.news .item{position:absolute;left:23px;width:220px}
.news .date{color:var(--crimson)}
.tick{position:absolute;width:0;height:0;border-left:6px solid transparent;border-right:6px solid transparent}
.events{left:847px;top:488px;width:253px;height:192px;background:var(--crimson);border-bottom-left-radius:14px;border-bottom-right-radius:14px;color:#fff}
.events .ptitle{position:absolute;left:63px;top:14px}
.events .item{position:absolute;left:23px;width:220px}
.side{left:851px;top:698px;width:163px;font-size:10px;font-weight:bold;color:#9c9c9c}
.side div{height:24px;border-bottom:1px dashed #ddd;padding-top:3px;padding-left:14px;position:relative}
.side div:before{content:"»";position:absolute;left:0;top:0;font-size:14px;color:#aaa}
.minilogo{left:852px;top:906px;display:flex;align-items:center;gap:8px;font-family:'Oswald',sans-serif;font-weight:300;line-height:1}
.minilogo .dot{width:46px;height:46px;border-radius:50%;border:4px solid #111}
.minilogo .n1{font-size:18px;color:var(--ink)}
.minilogo .n2{font-size:22px;color:var(--wine)}
.sidefade{left:833px;top:680px;width:14px;height:280px;background:linear-gradient(90deg,#f0f0f0,#fff)}
.h2{font-family:'Oswald',sans-serif;font-weight:300;font-size:19px;color:var(--crimson);letter-spacing:-.6px}
.copy{font-size:12px;line-height:14.5px;text-align:justify}
.rule{left:112px;top:629px;width:703px;height:1px;background:var(--line)}
.table{left:120px;top:724px;width:687px;height:228px;border:1px solid #b8b8b8;background:var(--panel);font-family:'Oswald',sans-serif;font-weight:300}
.col{position:absolute;top:0;bottom:0}
.col .head{height:35px;padding:7px 0 0 14px;font-size:17px;color:var(--wine);letter-spacing:-.5px;position:relative}
.col .head:after{content:"";position:absolute;right:10px;top:0;border-left:6px solid transparent;border-right:6px solid transparent;border-top:7px solid var(--wine)}
.col .row{height:24px;padding-left:13px;font-size:13px;color:var(--ink);letter-spacing:-.2px;white-space:nowrap}
.col .head+.row{margin-top:10px}
.c1{left:0;width:306px}.c1 .head{background:#eeeded}
.c2{left:306px;width:196px;background:#ececec}.c2 .head{background:#e2e2e2;padding-left:18px}.c2 .row{padding-left:18px}
.c3{left:502px;width:184px;background:#e4e4e4}.c3 .head{background:#d9d9d9;padding-left:9px}.c3 .row{padding-left:9px}
.footline{left:0;top:961px;width:1200px;height:1px;background:#cfcfcf}
.foot{font-size:11px;color:#666;white-space:nowrap}
.foot.addr{font-size:10.5px}
.follow{left:640px;top:977px;font-family:'Oswald',sans-serif;font-weight:300;font-size:14px;color:var(--wine);white-space:nowrap}
.footsocial{left:714px;top:981px;gap:10px;font-size:9.5px}
</style>
</head>
<body>
<div class="abs toplinks"><span>MY MARBLEFORK VALE</span><span>POLICE DEPARTMENT</span><span>CITY COUNCIL</span><span>FORM &amp; APPLICATIONS</span><span>FINANCIAL TRANSPARENCY</span></div>

<div class="abs seal">Marblefork<br>Vale</div>
<div class="abs title"><div class="t1">TOWN OF</div><div class="t2">MARBLEFORK VALE TEXAS</div></div>

<div class="abs phone">
<svg width="14" height="19" viewBox="0 0 14 19"><path d="M3 1h4l-1 5-2 1c0 3 1 5 3 6l2-1 3 3-2 3C5 17 1 12 2 4z" fill="#c0163a"/></svg>
817-555-0148</div>
<div class="abs social"><span>Chatterline</span><span>Friendsheet</span></div>

<div class="abs band"></div>
<div class="abs nav">
<span style="left:0">HOME</span><span style="left:90px">POLICE</span><span style="left:186px">CITY COUNCIL</span><span style="left:306px">ONLINE PAYMENTS</span><span style="left:446px">FAQ'S</span><span style="left:520px">CONTACT US</span><span style="left:630px">QUICK LINKS &#9656;</span>
</div>
<div class="tick" style="left:108px;top:199px;border-top:6px solid #fff"></div>
<div class="abs search">SEARCH<i></i></div>

<div class="abs photo" role="img" aria-label="Brick entrance wall with the town name sign, shrubs and palms in front"></div>

<div class="abs news">
<div class="tick" style="left:28px;top:0;border-top:7px solid var(--wine)"></div>
<div class="ptitle">LATEST NEWS MARBLEFORK</div>
<div class="item" style="top:49px"><span class="date">Sun, Oct. 7 - Wed, October 10</span><br>Regional City/County Administration Association Annual Conference</div>
<div class="item" style="top:106px"><span class="date">Wed, Oct. 31</span><br>Municipal Leaders Association of the Western Plains Annual Conference</div>
<svg class="abs" style="left:9px;top:172px" width="12" height="14"><path d="M10 1 3 7l7 6" stroke="#333" stroke-width="2.5" fill="none"/></svg>
<svg class="abs" style="left:230px;top:172px" width="12" height="14"><path d="M2 1l7 6-7 6" stroke="#333" stroke-width="2.5" fill="none"/></svg>
</div>

<div class="abs events">
<div class="tick" style="left:28px;top:2px;border-top:7px solid #fff"></div>
<div class="ptitle">UPCOMING EVENTS</div>
<div class="item" style="top:55px">Sun, Oct. 7 - Wed, October 10<br>Regional City/County Administration Association Annual Conference</div>
<div class="item" style="top:112px">Wed, Oct. 31<br>Municipal Leaders Association of the Western Plains Annual Conference</div>
</div>

<div class="abs sidefade"></div>
<div class="abs side">
<div>BOARDS &amp; COMMISSIONS</div><div>RELATED LINKS</div><div>LAND USE</div><div>ECONOMIC DEVELOPMENT</div><div>UTILITIES &amp; SERVICES</div><div>ONLINE PAYMENTS</div><div>FAQ'S</div><div>CONTACT US</div>
</div>
<div class="abs minilogo"><div class="dot"></div><div><div class="n1">TOWN OF</div><div class="n2">MARBLEFORK VALE</div></div></div>

<div class="abs h2" style="left:108px;top:499px">WHAT IS HAPPENING IN MARBLEFORK VALE?</div>
<p class="abs copy" style="left:112px;top:525px;width:710px">Neighborhood Night Out Event in Marblefork Vale on Tuesday, October 2nd. please reserve this date on your calendar! Come out and participate in a Neighborhood Night Out event at Town Hall on Tuesday, October 2nd. This event will be held in participation with the Brazos Hollow County Sheriff's Department and include surrounding communities. Neighborhood Night Out is designed to heighten crime and drug prevention awareness; generate support for, and participation in, local anti-crime programs; strengthen neighborhood spirit and police-community partnerships; and send a message to criminals letting them know that neighborhoods are organized and fighting back. More details to follow in the coming weeks.</p>
<div class="abs rule"></div>

<div class="abs h2" style="left:112px;top:640px">AGENDES &amp; MINUTES</div>
<p class="abs copy" style="left:114px;top:667px;width:698px;text-align:left">Quarry Dell Wells Agendas &amp; Minutes<br>Residents are welcome to attend Quarry Dell Wells City Council meetings, as well as other city board and commission meetings.</p>

<div class="abs table">
<div class="col c1"><div class="head">BOARD</div>
<div class="row">Animal Shelter Advisory Board</div><div class="row">Animal Shelter Advisory Board</div><div class="row">Animal Shelter Advisory Board</div><div class="row">Animal Shelter Advisory Board</div><div class="row">Animal Shelter Advisory Board</div><div class="row">Animal Shelter Advisory Board</div><div class="row">Animal Shelter Advisory Board</div></div>
<div class="col c2"><div class="head">AGENDAS</div>
<div class="row">Most Recent Agenda &nbsp;|&nbsp; View All</div><div class="row">Most Recent Agenda &nbsp;|&nbsp; View All</div><div class="row">Most Recent Agenda &nbsp;|&nbsp; View All</div><div class="row">Most Recent Agenda &nbsp;|&nbsp; View All</div><div class="row">Most Recent Agenda &nbsp;|&nbsp; View All</div><div class="row">Most Recent Agenda &nbsp;|&nbsp; View All</div><div class="row">Most Recent Agenda &nbsp;|&nbsp; View All</div></div>
<div class="col c3"><div class="head">MINUTES</div>
<div class="row">Most Recent Minutes &nbsp;|&nbsp; View All</div><div class="row">Most Recent Minutes &nbsp;|&nbsp; View All</div><div class="row">Most Recent Minutes &nbsp;|&nbsp; View All</div><div class="row">Most Recent Minutes &nbsp;|&nbsp; View All</div><div class="row">Most Recent Minutes &nbsp;|&nbsp; View All</div><div class="row">Most Recent Minutes &nbsp;|&nbsp; View All</div><div class="row">Most Recent Minutes &nbsp;|&nbsp; View All</div></div>
</div>

<div class="abs footline"></div>
<div class="abs foot" style="left:108px;top:978px">© 2007-2010 TOWN OF MARBLEFORK VALE, TEXAS.</div>
<div class="abs follow">FOLLOW US :</div>
<div class="abs social footsocial"><span>Chatterline</span><span>Friendsheet</span></div>
<div class="abs" style="left:830px;top:966px;width:1px;height:35px;background:#cfcfcf"></div>
<div class="abs foot addr" style="left:845px;top:967px">4120 CEDAR RIDGE RD. MARBLEFORK VALE, TX 76199</div>
<div class="abs foot addr" style="left:845px;top:988px">CALL US : 817-555-0148</div>
</body>
</html>
```